Stationary & Business Card for Talvo Co, LLC
Talvo Co, LLC
Professional
Adrian Pellworth, MD
President
2918 Larkfield Ave., Suite C-240
Bethesda, MD 20846
dradrian@talvocollc.com
www.talvocollc.com
Our tagline is Your Partner in Personalized Healthcare.
We would like a solid color for our back - either matching the purple or gold of our logo

```html
<!DOCTYPE html>
<html lang="en">
<head>
<meta charset="utf-8">
<title>Talvo Co, LLC — Business Card</title>
<link rel="stylesheet" href="https://fonts.googleapis.com/css2?family=Lato:wght@300;400;700&display=swap">
<style>
  :root {
    --purple: #4b2167;
    --purple-deep: #3a1752;
    --gold: #e0a820;
    --ink: #3b3b3b;
    --muted: #6d6d6d;
    --card: #ffffff;
    --on-purple: #ffffff;
    --backdrop: #e9e9ec;
  }
  * { box-sizing: border-box; margin: 0; padding: 0; }
  html, body {
    width: 1200px; height: 1002px; overflow: hidden;
    background: var(--backdrop);
    font-family: "Lato", Arial, sans-serif;
  }
  .canvas { position: relative; width: 1200px; height: 1002px; }
  .card {
    position: absolute; left: 210px;
    width: 780px; height: 446px;
    background: var(--card);
    border-radius: 22px;
    overflow: hidden;
    box-shadow: 0 6px 24px rgba(0,0,0,0.12);
  }
  .card--front { top: 35px; }
  .card--back { top: 521px; background: var(--purple); }

  /* front */
  .front-shapes { position: absolute; inset: 0; width: 100%; height: 100%; }
  .brand {
    position: absolute; left: 44px; top: 40px;
    display: flex; align-items: center; gap: 18px;
  }
  .brand-mark {
    width: 82px; height: 82px; border-radius: 50%;
    background: var(--purple); flex: none;
  }
  .brand-name {
    font-size: 44px; font-weight: 700; color: var(--purple);
    letter-spacing: 0.5px; line-height: 1;
  }
  .brand-tagline {
    margin-top: 8px; font-size: 12px; font-weight: 400;
    color: var(--muted); letter-spacing: 1.2px; text-transform: uppercase;
  }
  .contact-list {
    position: absolute; left: 44px; top: 150px;
    list-style: none;
    font-size: 13.5px; color: var(--ink); line-height: 1.25;
  }
  .contact-list li {
    display: flex; align-items: center; gap: 10px; margin-bottom: 7px;
  }
  .contact-icon {
    width: 18px; height: 18px; border-radius: 50%;
    background: var(--purple); flex: none;
    display: flex; align-items: center; justify-content: center;
  }
  .contact-icon--blank { background: transparent; }
  .contact-icon svg { width: 10px; height: 10px; fill: var(--on-purple); }
  .person {
    position: absolute; right: 48px; top: 296px; text-align: right;
  }
  .person-name { font-size: 19px; font-weight: 700; color: var(--purple); }
  .person-title { font-size: 14px; color: var(--muted); margin-top: 3px; }
  .front-url {
    position: absolute; right: 48px; bottom: 20px;
    font-size: 16px; color: var(--on-purple); letter-spacing: 3px;
  }

  /* back: solid purple */
  .back-mark {
    position: absolute; left: 50%; top: 108px;
    width: 150px; height: 150px; margin-left: -75px;
    border-radius: 50%; background: var(--gold);
  }
  .back-url {
    position: absolute; left: 0; right: 0; top: 300px;
    text-align center; text-align: center; font-size: 22px; color: var(--on-purple);
    letter-spacing: 5px; font-weight: 300;
  }
</style>
</head>
<body>
<main class="canvas">

  <section class="card card--front" aria-label="Business card front">
    <svg class="front-shapes" viewBox="0 0 780 446" preserveAspectRatio="none" aria-hidden="true">
      <path d="M0 316 L300 338 C420 346 520 352 780 362 L780 376 C520 368 420 362 300 356 L0 334 Z" fill="var(--gold)"/>
      <path d="M0 338 L300 360 C420 368 520 374 780 382 L780 446 L0 446 Z" fill="var(--purple)"/>
      <path d="M0 338 L0 360 C120 372 200 380 300 384 C200 378 120 366 0 338 Z" fill="var(--purple-deep)"/>
    </svg>

    <header class="brand">
      <span class="brand-mark"></span>
      <div>
        <div class="brand-name">Talvo Co, LLC</div>
        <div class="brand-tagline">Your Partner in Personalized Healthcare</div>
      </div>
    </header>

    <ul class="contact-list">
      <li><span class="contact-icon"><svg viewBox="0 0 10 10"><path d="M5 0a3.3 3.3 0 0 0-3.3 3.3C1.7 5.8 5 10 5 10s3.3-4.2 3.3-6.7A3.3 3.3 0 0 0 5 0zm0 4.6a1.3 1.3 0 1 1 0-2.6 1.3 1.3 0 0 1 0 2.6z"/></svg></span>2918 Larkfield Ave., Suite C-240</li>
      <li><span class="contact-icon contact-icon--blank"></span>Bethesda, MD 20846</li>
      <li><span class="contact-icon"><svg viewBox="0 0 10 10"><path d="M2 0.5l1.6 2.2-1 1c.6 1.3 1.5 2.2 2.8 2.8l1-1L8.6 7 8 9.3C4 9 1 6 .7 2L2 .5z"/></svg></span>(301) 555-0142</li>
      <li><span class="contact-icon"><svg viewBox="0 0 10 10"><rect x="1" y="3" width="8" height="5" rx="1"/><rect x="3" y="1" width="4" height="2"/></svg></span>(301) 555-0187</li>
      <li><span class="contact-icon"><svg viewBox="0 0 10 10"><path d="M0.5 2h9v6h-9z M0.5 2L5 5.5 9.5 2" stroke="#fff" stroke-width="0.9" fill="none"/></svg></span>dradrian@talvocollc.com</li>
      <li><span class="contact-icon"><svg viewBox="0 0 10 10"><circle cx="5" cy="5" r="4" stroke="#fff" stroke-width="0.9" fill="none"/><path d="M1 5h8M5 1c-2 2.5-2 5.5 0 8M5 1c2 2.5 2 5.5 0 8" stroke="#fff" stroke-width="0.8" fill="none"/></svg></span>www.talvocollc.com</li>
    </ul>

    <div class="person">
      <div class="person-name">Adrian Pellworth, MD</div>
      <div class="person-title">President</div>
    </div>

    <div class="front-url">www.talvocollc.com</div>
  </section>

  <section class="card card--back" aria-label="Business card back">
    <span class="back-mark"></span>
    <div class="back-url">www.talvocollc.com</div>
  </section>

</main>
</body>
</html>
```